Pre-workout label and Super Greens label for Vantora Nutrition Supplements

I need a label design for Club Vantora's 2 supplements. The first is a Pre-workout. The Pre-workout label needs to be 11.25 x 2.5 inches. This label will go on a black container. The second is a Super-Green. The Super-Green label should be 11.25 x 4.25 inches and will go on a white container. We have been selling these for a few years but the current labels are a little meh. I'd like something trendier and bolder. Must keep the Club Vantora branding. All the nurtition data must appear . I attached the current designs so you can know the flavors, nutrtional data etc. Thank you!
Updates

I can upload the Club Vantora logo! If anyone can tell me how to do that.

```html
<!DOCTYPE html>
<html lang="en">
<head>
<meta charset="utf-8">
<title>Vantora Nutrition – Pre Workout Label</title>
<link href="https://fonts.googleapis.com/css2?family=Audiowide&family=Exo+2:ital,wght@1,900&family=Montserrat:wght@600;700;800&family=Roboto:wght@400&display=swap" rel="stylesheet">
<style>
  :root{
    --red:#e3222d;
    --black:#1c1c1e;
    --ink:#0d0d0e;
    --white:#ffffff;
    --stage:#f1f1f2;
    --rule:#d9d9d9;
  }
  *{margin:0;padding:0;box-sizing:border-box}
  html,body{width:1200px;height:675px;overflow:hidden;background:var(--stage)}
  .label{
    position:absolute;left:20px;top:208px;width:1160px;height:258px;
    border-radius:10px;overflow:hidden;border:1.5px solid var(--red);
    font-family:"Montserrat",sans-serif;color:var(--white);
  }
  .label__bg{position:absolute;inset:0}
  .abs{position:absolute}

  /* back panel */
  .tag{
    background:var(--red);border-radius:6px;height:9px;width:96px;
    font-family:"Audiowide",sans-serif;font-size:7.2px;line-height:9px;
    padding-left:14px;letter-spacing:.6px;color:var(--white);
  }
  .directions-tag{left:26px;top:17px}
  .directions{left:24px;top:33px;width:232px;font-size:6.3px;font-weight:600;line-height:7px}
  .warning-tag{left:26px;top:61px}
  .warning{left:24px;top:79px;width:292px;font-size:6.3px;font-weight:600;line-height:7px;text-align:justify}
  .disclaimer{
    left:24px;top:200px;width:288px;height:37px;border:2px solid var(--ink);border-radius:6px;
    font-size:6.8px;font-weight:600;line-height:7px;text-align:center;padding:7px 26px 0;
  }

  /* front panel */
  .brand{left:496px;top:1px;width:200px;text-align:center}
  .brand__mark{width:44px;height:44px;background:var(--red);margin:0 auto 9px;border:1.5px solid var(--white)}
  .brand__name{font-family:"Audiowide",sans-serif;font-size:7.5px;letter-spacing:1px;color:var(--white)}
  .product{left:446px;top:70px;width:300px;text-align:center;font-family:"Exo 2",sans-serif;font-style:italic;font-weight:900;line-height:1}
  .product__pre{font-size:35px;color:var(--red)}
  .product__name{font-size:38px;color:var(--white);margin-top:-2px}
  .flavor{
    left:490px;top:155px;width:201px;height:25px;
    border:2px solid var(--ink);border-radius:7px;background:var(--red);
    font-family:"Audiowide",sans-serif;font-size:11.5px;letter-spacing:1.2px;text-align:center;line-height:21px;
  }
  .benefit{top:194px;width:60px;text-align:center}
  .benefit svg{display:block;margin:0 auto}
  .benefit__name{font-family:"Audiowide",sans-serif;font-size:5.6px;letter-spacing:.4px;margin-top:4px}
  .benefit__sub{font-size:4.2px;font-weight:600;line-height:4.5px}
  .energy{left:498px}.performance{left:557px}.strength{left:617px}
  .meta{left:500px;top:244px;width:170px;font-size:6.5px;font-weight:800;letter-spacing:.2px;text-align:center}
  .meta__sep{display:inline-block;width:1px;height:8px;background:var(--white);vertical-align:middle;margin:0 7px}
  .servings{left:667px;top:216px;width:72px;text-align:center}
  .servings__num{font-family:"Audiowide",sans-serif;font-size:27px;line-height:25px;color:var(--red)}
  .servings__word{font-family:"Audiowide",sans-serif;font-size:6.5px;letter-spacing:.6px}

  /* supplement facts */
  .facts{left:847px;top:18px;width:289px;height:188px;background:var(--ink);border-radius:6px;overflow:hidden}
  .facts__head{height:29px;background:var(--red);font-family:"Montserrat",sans-serif;font-weight:800;font-size:16px;text-align:center;line-height:29px;letter-spacing:.3px}
  .facts__serving{font-family:"Roboto",sans-serif;font-size:6px;line-height:7.5px;padding:5px 0 0 7px}
  .facts__table{margin:3px 7px 0 6px;width:276px;border-collapse:collapse;font-family:"Roboto",sans-serif;font-size:6px}
  .facts__table th{font-weight:400;text-align:left;border-top:1.5px solid var(--rule);border-bottom:1.5px solid var(--rule);height:10px}
  .facts__table td{border-bottom:.6px solid var(--rule);height:9.5px;line-height:8px}
  .facts__table .thick td{border-bottom:1.5px solid var(--rule)}
  .facts__table .dv{text-align:right}
  .facts__note{font-family:"Roboto",sans-serif;font-size:6px;padding:3px 0 0 7px}
  .ingredients{left:857px;top:221px;width:280px;font-size:5.8px;font-weight:700;line-height:6.5px}
  .formulated{left:857px;top:240px;width:280px;font-size:5.8px;font-weight:700}
</style>
</head>
<body>
<main class="label" aria-label="Vantora Nutrition Pre Workout label">
  <svg class="label__bg" width="1160" height="258" viewBox="0 0 1160 258" aria-hidden="true">
    <defs>
      <linearGradient id="topRule" x1="0" x2="1">
        <stop offset="0" stop-color="#ffffff"/><stop offset="1" stop-color="#6b6b6b"/>
      </linearGradient>
    </defs>
    <rect width="1160" height="258" fill="var(--black)"/>
    <rect x="615" y="0" width="545" height="4" fill="url(#topRule)"/>
    <path d="M0 181 H420 C452 181 450 140 492 140 H770 C812 140 812 181 848 181 H1160 V258 H0 Z" fill="var(--red)"/>
    <path d="M661 258 L676 215 H728 L744 258 Z" fill="var(--ink)"/>
  </svg>

  <div class="abs tag directions-tag">DIRECTIONS:</div>
  <p class="abs directions">Use on training days only. Mix 1 scoop with 6–8 oz of cold water 15–30 minutes prior to training.</p>
  <div class="abs tag warning-tag">WARNING:</div>
  <p class="abs warning">Not intended for use by persons under age 18. Do not exceed recommended dose. Do not consume synephrine or caffeine from other sources, including but not limited to: coffee, tea, soda, and other dietary supplements or medications containing phenylephrine or caffeine. Contains caffeine. Use in a 12 week on, 2 week off pattern. Consult your physician prior to use if you are pregnant or nursing, or if you are taking medication, including but not limited to: MAOI inhibitors, antidepressants, aspirin, non-steroidal, anti-inflammatory drugs or products containing phenylephrine, ephedrine, pseudoephedrine, or other stimulants. Consult your physician prior to use if you have a medical condition, including but not limited to: heart, liver, kidney, or thyroid disease, cardiac arrhythmia, recurrent headaches, enlarged prostate or glaucoma. Discontinue use 2 weeks prior to surgery or if you experience rapid heartbeat, dizziness, severe headaches, or shortness of breath. This product DOES NOT contain ingredients banned by certain sports organizations.</p>
  <p class="abs disclaimer">*These statements have not been evaluated by the Food and Drug Administration. This product is not intended to diagnose, treat, cure or prevent any disease.</p>

  <div class="abs brand">
    <div class="brand__mark"></div>
    <div class="brand__name">VANTORA NUTRITION</div>
  </div>
  <h1 class="abs product"><div class="product__pre">PRE</div><div class="product__name">WORKOUT</div></h1>
  <div class="abs flavor">WATERMELON SUGAR</div>

  <div class="abs benefit energy">
    <svg width="22" height="22" viewBox="0 0 22 22" aria-hidden="true"><path d="M2 2H20V15L11 20 2 15Z" fill="var(--red)" stroke="var(--ink)" stroke-width="2"/><path d="M12 4 7 12H11L9 17 15 9H11Z" fill="var(--white)"/></svg>
    <div class="benefit__name">ENERGY*</div><div class="benefit__sub">(Caffeine)</div>
  </div>
  <div class="abs benefit performance">
    <svg width="22" height="22" viewBox="0 0 22 22" aria-hidden="true"><path d="M2 2H20V15L11 20 2 15Z" fill="var(--red)" stroke="var(--ink)" stroke-width="2"/><path d="M11 4 16 10H13V16H9V10H6Z" fill="var(--white)"/></svg>
    <div class="benefit__name">PERFORMANCE*</div><div class="benefit__sub">(Beta-alanine)</div>
  </div>
  <div class="abs benefit strength">
    <svg width="22" height="22" viewBox="0 0 22 22" aria-hidden="true"><path d="M2 2H20V15L11 20 2 15Z" fill="var(--red)" stroke="var(--ink)" stroke-width="2"/><path d="M5 7H7.5V14H5ZM14.5 7H17V14H14.5ZM7.5 9.5H14.5V11.5H7.5Z" fill="var(--white)"/></svg>
    <div class="benefit__name">STRENGTH*</div><div class="benefit__sub">(Creatine)</div>
  </div>
  <div class="abs meta">DIETARY SUPPLEMENT<span class="meta__sep"></span>240G (8.5OZ)</div>
  <div class="abs servings"><div class="servings__num">30</div><div class="servings__word">SERVINGS</div></div>

  <section class="abs facts">
    <h2 class="facts__head">SUPPLEMENT FACTS</h2>
    <p class="facts__serving">Serving Size: 1 Scoop (8 g)<br>Servings per Container: 30</p>
    <table class="facts__table">
      <tr><th style="width:125px"></th><th>Amount per Serving</th><th class="dv">%DV</th></tr>
      <tr><td>Vitamin C (Ascorbic Acid)</td><td>250mg</td><td class="dv">278%</td></tr>
      <tr><td>Vitamin B6 (as Pyridoxal-5'-Phosphate)</td><td>0.035 mg</td><td class="dv">2%</td></tr>
      <tr><td>Folate</td><td>250 mcg DFE (150 mcg Folic Acid)</td><td class="dv">63%</td></tr>
      <tr><td>Vitamin B12 (as Methylcobalamin)</td><td>20 mcg</td><td class="dv">833%</td></tr>
      <tr class="thick"><td>Calcium (as Calcium Silicate)</td><td>18.30 mg</td><td class="dv">1%</td></tr>
      <tr><td>Beta-Alanine</td><td>1.5 g</td><td class="dv">†</td></tr>
      <tr><td>Creatine Monohydrate</td><td>1 g</td><td class="dv">†</td></tr>
      <tr><td>L-Arginine Alpha-Ketoglutarate</td><td>1 g</td><td class="dv">†</td></tr>
      <tr><td>L-Citrulline Malate</td><td>1 g</td><td class="dv">†</td></tr>
      <tr><td>N-Acetyl L-Tyrosine</td><td>500 mg</td><td class="dv">†</td></tr>
      <tr><td>Caffeine Anhydrous</td><td>250 mg</td><td class="dv">†</td></tr>
      <tr class="thick"><td>Synephrine HCl</td><td>30 mg</td><td class="dv">†</td></tr>
    </table>
    <p class="facts__note">† Daily Value (DV) not established</p>
  </section>
  <p class="abs ingredients">Other Ingredients: Citric Acid, Pineapple Fruit Juice Powder, Silicon Dioxide, Natural and Artificial Flavors, Acesulfame Potassium, Sucralose, and FD&amp;C Red #40.</p>
  <p class="abs formulated">Formulated by: Club Vantora, 250 Ridge Rd Fairview, WY 82000 (555) 010-4821</p>
</main>
</body>
</html>
```